依頼詳細
米袋パッケージデザインの依頼をさせて頂きます。
今回、特に希望する方向性はございません。

自由度がかなり高く、曖昧な部分がある為デザインが難しいかと思われますが、
どうか力をお貸しください。

・高級感、シンプルさ、オシャレな感じ、ポップな感じ、
そよ凪や宵月の調べ・岳兵衛などの統一デザインっぽさ、
など方向性は自由です。
・洋風、和風など自由です。
・写真、イラスト、フォント自由です。筆文字可。(版権等にご注意ください。)
・色も自由です。金色銀色使用可能です。

良いと思うデザイン例
・コンセプトやデザインに一捻りあるもの。
(絶対に必要というわけではありません。)
・特別感。(絶対に必要というわけではありません。)

悪いと思うデザイン例
・スーパーによく置いてあるような安っぽい感じ。

■デザイン上に必ず入れて欲しいもの■
※すべて「」は必要ありません。

・「新潟県産」※新潟や新潟産でもかまいません。
・「こしひかり」※カタカナでもかまいません。
・「5kg」
・「中のお米が見える部分」

印刷適正・文字などはデザイン決定後こちらで調整致しますので
背景や全体のデザインイメージを重要視します。

・修正作業をお願いすることはありません。
・ご提案をして頂く際に、袋に印刷されたように見える
擬似実物処理(立体)などは不要です。
平面画像のみで公平に判断したいと考えております。
記載項目
サイズ:W300mm×H470mm
グラビア印刷/ラミネート加工

```html
<!DOCTYPE html>
<html lang="ja">
<head>
<meta charset="utf-8">
<title>新潟県産 コシヒカリ 5kg</title>
<link href="https://fonts.googleapis.com/css2?family=Shippori+Mincho:wght@400;500;600&display=swap" rel="stylesheet">
<style>
  :root {
    --paper: #f7f3ec;
    --ink: #2b2623;
    --soft-green: #dfe8d6;
    --soft-pink: #f1dcd6;
    --soft-cream: #efe6d3;
    --soft-blue: #dde6e8;
    --stamp-tint: #e9c9c2;
    --rice-light: #efe7d7;
    --rice-dark: #d9cbb0;
    --label-white: #ffffff;
  }
  * { margin: 0; padding: 0; box-sizing: border-box; }
  html, body { width: 766px; height: 1200px; overflow: hidden; background: var(--paper); }
  .package {
    position: relative;
    width: 766px; height: 1200px;
    overflow: hidden;
    font-family: "Shippori Mincho", serif;
    color: var(--ink);
  }
  .stalk-illustration {
    position: absolute; inset: 0;
    background:
      linear-gradient(90deg,
        var(--soft-pink) 0 6%, var(--paper) 6% 14%,
        var(--soft-green) 14% 20%, var(--paper) 20% 30%,
        var(--soft-cream) 30% 36%, var(--paper) 36% 64%,
        var(--soft-blue) 64% 70%, var(--paper) 70% 80%,
        var(--soft-green) 80% 86%, var(--paper) 86% 94%,
        var(--soft-pink) 94% 100%);
    opacity: 0.85;
  }
  .tagline {
    position: absolute;
    top: 38px; right: 52px;
    writing-mode: vertical-rl;
    font-size: 25px;
    line-height: 1.5;
    letter-spacing: 0.1em;
    font-weight: 500;
  }
  .name-label {
    position: absolute;
    left: 243px; top: 191px;
    width: 306px; height: 689px;
    border-radius: 50%;
    background: var(--label-white);
    border: 3px solid var(--ink);
  }
  .region-arc {
    position: absolute;
    left: 0; top: 0;
    width: 766px; height: 1200px;
  }
  .region-arc text {
    font-family: "Shippori Mincho", serif;
    font-size: 24px;
    letter-spacing: 5px;
    fill: var(--ink);
  }
  .variety-name {
    position: absolute;
    left: 396px; top: 280px;
    transform: translateX(-50%);
    writing-mode: vertical-rl;
    font-size: 98px;
    line-height: 1;
    letter-spacing: 0.1em;
    font-weight: 500;
  }
  .origin {
    position: absolute;
    writing-mode: vertical-rl;
    font-size: 36px;
    line-height: 1;
    letter-spacing: 0.15em;
    font-weight: 500;
  }
  .origin-prefecture { left: 462px; top: 522px; }
  .origin-grown { left: 306px; top: 508px; }
  .net-weight {
    position: absolute;
    left: 396px; top: 820px;
    transform: translateX(-50%);
    font-size: 34px;
    font-weight: 500;
    line-height: 1;
  }
  .net-weight small { font-size: 22px; }
  .origin-stamp {
    position: absolute;
    left: 14px; top: 880px;
    width: 90px; height: 130px;
    border-radius: 6px;
    background: var(--stamp-tint);
  }
  .rice-window {
    position: absolute;
    left: 322px; top: 1005px;
    width: 148px; height: 90px;
    border-radius: 40px;
    background: radial-gradient(ellipse at 50% 45%, var(--rice-light), var(--rice-dark));
  }
</style>
</head>
<body>
  <main class="package">
    <div class="stalk-illustration" role="img" aria-label="淡い色の縦縞に稲穂が揺れる背景イラスト"></div>

    <p class="tagline">炊き上がりが、<br>待ち遠しくなる<br>お米です。</p>

    <div class="name-label"></div>

    <svg class="region-arc" viewBox="0 0 766 1200" aria-hidden="true">
      <defs>
        <path id="arc-path" d="M 236 345 Q 248 232 336 168"/>
      </defs>
      <text><textPath href="#arc-path">NIIGATA</textPath></text>
    </svg>

    <h1 class="variety-name">コシヒカリ</h1>
    <p class="origin origin-prefecture">新潟</p>
    <p class="origin origin-grown">県産</p>
    <p class="net-weight">5<small>kg</small></p>

    <div class="origin-stamp" role="img" aria-label="産地を示す朱色の印の装飾"></div>

    <div class="rice-window" role="img" aria-label="中のお米が見える透明窓"></div>
  </main>
</body>
</html>
```